CoverLantern.com website re-design - modern engaging website creation

We have an existing website. Www.CoverLantern.com - the content on the site and our widgets are custom built. But the layout and design of our site we just put there as we built the functionality around it. We want a new, bold, and modern design aimed at getting visitors to run a life insurance quote and ultimately apply. Our demographic is centered around those between the ages of 30-60. So we are looking at a complete site overhaul with better pictures, buttons, and an extremely modern design.

Target Market(s)

30-50 year olds

Industry/Entity Type

Life insurance

Coding

Coded - Design and coding required

Number of Pages Required

5+ page

Font styles to use
Other font styles liked:
• Rubik

Colors
0054AA
0677BA
7BADD7
CADEEF
E8F1F8
00AB8E
00BBA5
67D7C9
C6EFE9
E9F9F6
59FF00
82FF00
B8FF75
E3FFCB
F4FFEA

Requirements
Must have
• Matching color schemes from existing website. We have custom widgets on our site now and those must be . White space is important to make it simple for the user to navigate
Nice to have
• Same content - different more modern design
Should not have
• Colors outside of our current color scheme. Should NOT be too similar to our existing site.

```html
<!DOCTYPE html>
<html lang="en">
<head>
<meta charset="utf-8">
<title>CoverLantern – Life Insurance Quotes</title>
<link href="https://fonts.googleapis.com/css2?family=Rubik:wght@300;400;500;700&display=swap" rel="stylesheet">
<style>
:root{
  --blue-dark:#0054AA;
  --blue:#0677BA;
  --blue-mid:#7BADD7;
  --blue-light:#CADEEF;
  --blue-pale:#E8F1F8;
  --teal:#00AB8E;
  --lime:#59FF00;
  --lime-2:#82FF00;
  --lime-soft:#B8FF75;
  --lime-pale:#F4FFEA;
  --ink:#1d2a3a;
  --muted:#6b7785;
  --white:#ffffff;
}
*{box-sizing:border-box;margin:0;padding:0}
html,body{width:1200px;height:2464px;overflow:hidden;background:var(--white)}
body{font-family:"Rubik",Arial,sans-serif;color:var(--ink)}
.page{position:relative;width:1200px;height:2464px;overflow:hidden}

/* header */
.site-header{height:104px;padding:0 70px;display:flex;justify-content:space-between;align-items:center}
.brand{display:flex;align-items:center;gap:10px;font-size:34px;font-weight:500;color:var(--blue-dark)}
.brand-dot{width:14px;height:14px;border-radius:50%;background:var(--lime-2)}
.header-right{display:flex;flex-direction:column;align-items:flex-end;gap:14px}
.top-bar{display:flex;align-items:center;gap:12px;font-size:13px;color:var(--ink)}
.btn{display:inline-block;border-radius:4px;font-weight:500;letter-spacing:.5px;color:var(--white);text-transform:uppercase}
.btn-small{font-size:11px;padding:7px 14px}
.btn-green{background:var(--teal)}
.btn-blue{background:var(--blue-dark)}
.main-nav{display:flex;gap:42px;font-size:12px;font-weight:500;color:var(--ink);letter-spacing:.6px}

/* hero */
.hero{position:relative;height:470px;background:linear-gradient(110deg,#5b6b62 0%,#8e9a86 35%,#c6c3b4 65%,#e5e0d3 100%)}
.hero-text{position:absolute;left:70px;top:96px;color:var(--white);max-width:440px}
.hero-title{font-size:42px;font-weight:700;letter-spacing:1px}
.hero-sub{margin-top:10px;font-size:21px;line-height:1.3;color:var(--lime-soft)}
.hero .btn{margin-top:24px;font-size:12px;padding:11px 22px}
.hero-wave{position:absolute;left:0;bottom:-1px;width:1200px;height:110px}

/* how it works */
.how{padding:40px 70px 0;text-align:center}
.section-title{font-size:30px;font-weight:500;color:var(--ink)}
.section-title span{color:var(--blue-dark)}
.steps{margin-top:34px;display:flex;justify-content:space-between}
.step{width:184px;height:150px;border:1px solid var(--blue-light);border-radius:4px;display:flex;flex-direction:column;align-items:center;justify-content:center;gap:16px;font-size:14px;color:var(--ink)}
.step.active{background:var(--lime-2);border-color:var(--lime-2);color:var(--blue-dark);font-weight:500}
.step svg{width:46px;height:46px}

/* life insurance */
.life{display:flex;justify-content:space-between;align-items:center;padding:60px 120px 0 200px}
.life-text{width:380px}
.life-title{font-size:26px;font-weight:500;color:var(--blue-dark)}
.life-text p{margin-top:14px;font-size:14px;line-height:1.6;color:var(--muted)}
.life-text .btn{margin-top:20px;font-size:11px;padding:10px 18px}
.life-art{width:330px;height:260px;border-radius:50%;background:radial-gradient(circle,var(--blue-pale) 0%,var(--blue-light) 60%,#fff 72%)}

/* compare */
.compare{position:relative;margin-top:40px;height:380px;background:var(--blue-pale);text-align:center}
.compare-wave-top,.compare-wave-bottom{position:absolute;left:0;width:1200px;height:100px}
.compare-wave-top{top:-1px}
.compare-wave-bottom{bottom:-1px}
.compare-body{position:relative;padding-top:140px}
.compare-body p{width:430px;margin:12px auto 0;font-size:14px;line-height:1.6;color:var(--muted)}
.compare-body .btn{margin-top:20px;font-size:11px;padding:10px 18px}

/* partners */
.partners{display:flex;justify-content:space-between;align-items:center;padding:70px 90px 0}
.partner-badge{width:130px;height:44px;border-radius:6px;background:var(--blue-light)}

/* footer */
.site-footer{position:absolute;left:0;top:1830px;width:1200px;height:634px;background:var(--blue-pale)}
.footer-wave{position:absolute;top:-60px;left:0;width:1200px;height:90px}
.footer-cols{display:flex;padding:80px 70px 0;gap:80px}
.footer-contact{width:380px;font-size:14px;line-height:1.9;color:var(--ink)}
.footer-contact .brand{margin-bottom:18px}
.footer-heading{font-size:17px;font-weight:500;color:var(--blue-dark);margin-bottom:16px}
.footer-links{list-style:none;font-size:14px;line-height:2.1;color:var(--ink)}
.subscribe-field{width:240px;height:40px;border:1px solid var(--blue-mid);border-radius:4px;background:var(--white);font-size:13px;color:var(--muted);padding:11px 14px}
.subscribe .btn{margin-top:12px;font-size:11px;padding:9px 18px}
.social{display:flex;gap:10px;margin-top:22px}
.social span{width:30px;height:30px;border-radius:50%;background:var(--blue-dark)}
.footer-bottom{position:absolute;left:70px;right:70px;bottom:40px;border-top:1px solid var(--blue-light);padding-top:20px;display:flex;justify-content:space-between;font-size:12px;color:var(--muted)}
.footer-bottom nav{display:flex;gap:28px}
</style>
</head>
<body>
<div class="page">

  <header class="site-header">
    <div class="brand"><span>CoverLantern</span></div>
    <div class="header-right">
      <div class="top-bar">
        <span>Call: 1-800-555-0142</span>
        <span class="btn btn-small btn-green">Customer Service</span>
        <span class="btn btn-small btn-blue">Login</span>
      </div>
      <nav class="main-nav">
        <span>FIND QUOTES</span><span>ARTICLES</span><span>SERVICES</span><span>FAQ'S</span><span>ABOUT US</span><span>CONTACT US</span>
      </nav>
    </div>
  </header>

  <section class="hero" role="img" aria-label="Family with children smiling together on a sofa at home">
    <div class="hero-text">
      <h1 class="hero-title">ONLINE QUOTES</h1>
      <p class="hero-sub">Best Prices for Term Life Insurance from America's Top Rated Carriers</p>
      <span class="btn btn-blue">Get Started Now</span>
    </div>
    <svg class="hero-wave" viewBox="0 0 1200 110" preserveAspectRatio="none" aria-hidden="true">
      <path d="M0 70 C250 20 450 110 700 70 S1050 10 1200 50 L1200 110 L0 110Z" fill="var(--lime-2)"/>
      <path d="M0 85 C260 40 460 120 710 85 S1050 30 1200 68 L1200 110 L0 110Z" fill="#fff"/>
    </svg>
  </section>

  <section class="how">
    <h2 class="section-title">How <span>CoverLantern</span> Works</h2>
    <div class="steps">
      <div class="step active">
        <svg viewBox="0 0 46 46" fill="none" stroke="var(--blue-dark)" stroke-width="2.5"><rect x="9" y="5" width="28" height="36" rx="3"/><path d="M15 15h16M15 23h16M15 31h10"/></svg>
        Get an Instant Quote
      </div>
      <div class="step">
        <svg viewBox="0 0 46 46" fill="none" stroke="var(--teal)" stroke-width="2.5"><path d="M23 6v34M10 14h26M10 14l-5 12h10zM36 14l-5 12h10zM15 40h16"/></svg>
        Compare and Save
      </div>
      <div class="step">
        <svg viewBox="0 0 46 46" fill="none" stroke="var(--teal)" stroke-width="2.5"><rect x="6" y="8" width="34" height="24" rx="3"/><path d="M16 40h14M23 32v8"/></svg>
        Virtual Agent
      </div>
      <div class="step">
        <svg viewBox="0 0 46 46" fill="none" stroke="var(--teal)" stroke-width="2.5"><path d="M10 8h8l3 9-5 3c2 5 5 8 10 10l3-5 9 3v8c0 2-2 4-4 4C18 40 6 28 6 12c0-2 2-4 4-4z"/></svg>
        Live Agent Support
      </div>
      <div class="step">
        <svg viewBox="0 0 46 46" fill="none" stroke="var(--teal)" stroke-width="2.5"><rect x="9" y="5" width="28" height="36" rx="3"/><path d="M16 23l5 5 10-10"/></svg>
        Apply Online
      </div>
    </div>
  </section>

  <section class="life">
    <div class="life-text">
      <h2 class="life-title">Life Insurance Online</h2>
      <p>Compare quotes from top rated carriers in minutes. Pick your plan and apply online today.</p>
      <span class="btn btn-blue">Get Started</span>
    </div>
    <div class="life-art" role="img" aria-label="Illustration of a person beside a large insurance policy document"></div>
  </section>

  <section class="compare">
    <svg class="compare-wave-top" viewBox="0 0 1200 100" preserveAspectRatio="none" aria-hidden="true">
      <path d="M0 0 L1200 0 L1200 30 C950 90 700 10 450 60 S100 70 0 40Z" fill="#fff"/>
      <path d="M0 40 C100 70 250 80 450 60 S950 90 1200 30" fill="none" stroke="var(--lime-2)" stroke-width="6"/>
    </svg>
    <div class="compare-body">
      <h2 class="section-title">Compare <span>Quotes</span></h2>
      <p>Simple tools let you compare term life rates side by side, so you can find the coverage that fits your family and budget.</p>
      <span class="btn btn-blue">Get Started Now</span>
    </div>
    <svg class="compare-wave-bottom" viewBox="0 0 1200 100" preserveAspectRatio="none" aria-hidden="true">
      <path d="M0 60 C300 10 600 90 900 50 S1150 30 1200 50 L1200 100 L0 100Z" fill="#fff"/>
      <path d="M0 60 C300 10 600 90 900 50 S1150 30 1200 50" fill="none" stroke="var(--lime-2)" stroke-width="6"/>
    </svg>
  </section>

  <section class="partners" aria-label="Partner carriers">
    <span class="partner-badge"></span><span class="partner-badge"></span><span class="partner-badge"></span>
    <span class="partner-badge"></span><span class="partner-badge"></span><span class="partner-badge"></span>
  </section>

  <footer class="site-footer">
    <svg class="footer-wave" viewBox="0 0 1200 90" preserveAspectRatio="none" aria-hidden="true">
      <path d="M0 60 C300 10 700 90 1200 30 L1200 90 L0 90Z" fill="var(--blue-dark)"/>
      <path d="M0 72 C300 25 700 100 1200 45 L1200 90 L0 90Z" fill="var(--blue-pale)"/>
    </svg>
    <div class="footer-cols">
      <div class="footer-contact">
        <div class="brand"><span>CoverLantern</span></div>
        <div>1-800-555-0142</div>
        <div>hello@coverlantern.com</div>
        <div>450 Harbor Point Road, Suite 200</div>
        <div>Lakeview, OH 44012</div>
        <div>Monday – Friday, 9am – 6pm</div>
      </div>
      <div>
        <h3 class="footer-heading">Insurance Products</h3>
        <ul class="footer-links">
          <li>Term Life Insurance</li><li>Whole Life Insurance</li><li>Final Expense</li><li>No Exam Life</li><li>Senior Life Plans</li>
        </ul>
      </div>
      <div class="subscribe">
        <h3 class="footer-heading">Subscribe Us</h3>
        <div class="subscribe-field">Your email address</div>
        <span class="btn btn-blue">Subscribe</span>
        <div class="social"><span></span><span></span><span></span></div>
      </div>
    </div>
    <div class="footer-bottom">
      <span>© 2024 CoverLantern. All Rights Reserved.</span>
      <nav><span>Website Disclaimer</span><span>Privacy Policy</span><span>Terms of Use</span></nav>
    </div>
  </footer>

</div>
</body>
</html>
```